Foldable creative restaurant menu

We require foldable restaurant menu to be placed on the each table, want it to look creative and modern with pages representing pictures of the dish not all dishes but few to represent what we do.Please get creative make sure its different, the colour should represent classy restaurant, not cheap and fast. The shape of the menu can be difference creative words must be easy to read and the logo must be in the menu here and there briefly.

Target Market(s)

Restaurant customers

Industry/Entity Type

Health And Wellness

Colors

Designer to choose colors to be used in the design.

Requirements
Must have
• foldable, must have good dish presentation pictures and must look modern and classy
Nice to have
• funky design and creative can be not just square foldable but can be interesting shape of menu.
Should not have
• boring plain spaces
• small writing
• dark pictures

```html
<!DOCTYPE html>
<html lang="en">
<head>
<meta charset="utf-8">
<title>Veranda Restaurant – Tri-fold Menu</title>
<link href="https://fonts.googleapis.com/css2?family=Lato:wght@300;400&family=Montserrat:wght@400;500;600;700;800&display=swap" rel="stylesheet">
<style>
  :root{
    --red:#e3262f;
    --ink:#1d1d1d;
    --body:#4a4a4a;
    --paper:#ffffff;
    --stage:#ececec;
    --rose:#ec7b6c;
  }
  *{box-sizing:border-box;margin:0;padding:0}
  html,body{width:1200px;height:1200px;overflow:hidden}
  body{background:var(--stage);font-family:'Montserrat',sans-serif;color:var(--body);position:relative}

  .brochure{position:absolute;left:30px;top:160px;width:1140px;height:880px;background:var(--paper);overflow:hidden;box-shadow:0 6px 24px rgba(0,0,0,.12)}
  .fold{position:absolute;top:0;bottom:0;width:1px;background:rgba(0,0,0,.08);z-index:6}

  .panel-bg{position:absolute;top:0;height:880px;width:380px;
    background:linear-gradient(180deg,#e4e4e4 0%,#bdbdbd 35%,#a6a6a6 60%,#d8b0a8 82%,var(--rose) 100%)}
  .panel-bg.left{left:0}
  .panel-bg.middle{left:380px;background:linear-gradient(180deg,#f4f4f4 0%,#cfcfcf 40%,#b3b3b3 65%,#e2a79c 85%,var(--rose) 100%)}

  .menu-card{position:absolute;background:var(--paper);border-radius:14px;padding:20px;z-index:3;box-shadow:0 2px 10px rgba(0,0,0,.08)}
  .menu-card.breakfast{left:28px;top:36px;width:314px;height:640px}
  .menu-card.lunch{left:400px;top:36px;width:236px;height:530px;padding:18px 16px}

  .section-title{font-weight:700;color:var(--red);font-size:14px;letter-spacing:.3px;text-transform:uppercase;margin-top:10px}
  .dish{margin-top:7px}
  .dish-name{font-weight:700;color:var(--red);font-size:11px;text-transform:uppercase}
  .dish-desc{font-size:9px;line-height:1.3;color:var(--body)}
  .acai-list{list-style:none;margin-top:3px}
  .acai-list li{font-size:9px;line-height:1.25;display:flex;gap:5px;margin-top:3px}
  .num{flex:none;width:12px;height:12px;border-radius:50%;background:var(--red);color:#fff;font-size:8px;font-weight:700;display:flex;align-items:center;justify-content:center}
  .acai-list b{color:var(--red);font-weight:600}
  .price-row{display:flex;align-items:flex-end;font-size:9px;margin-top:2px}
  .price-row .label{color:var(--red);font-weight:600;text-transform:uppercase;font-size:8.5px}
  .price-row .leader{flex:1;border-bottom:1px solid #777;margin:0 5px 3px}
  .price-row .price{color:var(--ink);font-weight:500}

  .photo{position:absolute;border-radius:50%;z-index:4}
  .photo.fries{left:40px;top:690px;width:200px;height:200px;background:radial-gradient(circle at 45% 45%,#f2c75a 0%,#d79a35 45%,#8a6a45 80%,#6e7a54 100%)}
  .photo.salad{left:515px;top:572px;width:190px;height:190px;background:radial-gradient(circle at 50% 45%,#e58a3a 0%,#6ea446 30%,#3f7a34 65%,#f1f1f1 88%)}
  .photo.steak{left:405px;top:690px;width:170px;height:170px;background:radial-gradient(circle at 45% 50%,#9c4a2c 0%,#6e2d1c 40%,#5d8e3a 62%,#e9e6df 90%)}
  .rings{position:absolute;left:0;top:0;z-index:5;pointer-events:none}

  .brand{position:absolute;font-family:'Lato',sans-serif;color:var(--ink);z-index:3;line-height:1}
  .brand .name{font-weight:300;letter-spacing:4px}
  .brand .sub{font-weight:400;letter-spacing:3px;display:block;margin-top:6px}
  .brand.small{left:656px;top:58px}
  .brand.small .name{font-size:20px;letter-spacing:2px}
  .brand.small .sub{font-size:8px;letter-spacing:2px}
  .brand.cover{left:850px;top:44px}
  .brand.cover .name{font-size:34px}
  .brand.cover .sub{font-size:12px}

  .headline{position:absolute;left:872px;top:132px;z-index:3;line-height:1}
  .headline .light{display:block;font-family:'Lato',sans-serif;font-weight:300;font-size:38px;color:var(--ink);letter-spacing:-.5px}
  .headline .bold{display:block;font-weight:800;font-size:58px;color:var(--red);letter-spacing:-1px;margin-top:2px}

  .web{position:absolute;left:912px;top:250px;width:210px;padding:10px 0;border-top:1px solid #bbb;border-bottom:1px solid #bbb;text-align:center;font-family:'Lato',sans-serif;font-size:12.5px;letter-spacing:2.5px;color:var(--ink);z-index:3}

  .contact{position:absolute;left:670px;top:300px;width:250px;z-index:7;color:#fff}
  .contact h2{font-size:16px;font-weight:600;color:var(--red);margin-bottom:8px;padding-left:22px}
  .contact-row{display:flex;align-items:flex-start;gap:8px;font-size:12.5px;font-weight:600;line-height:1.25;margin-top:5px}
  .contact-row svg{flex:none;width:14px;height:14px;margin-top:1px}

  .hero-dish{position:absolute;left:790px;top:470px;width:400px;height:420px;border-radius:50% 0 0 50%;z-index:2;
    background:radial-gradient(circle at 45% 45%,#8fb35a 0%,#d9a13b 22%,#c5682b 42%,#a8442a 58%,#f3eee8 76%,#ffffff 90%)}
</style>
</head>
<body>
<div class="brochure">

  <div class="panel-bg left" role="img" aria-label="Soft-focus black and white photo of plated dishes fading to warm red"></div>
  <div class="panel-bg middle" role="img" aria-label="Soft-focus photo of a restaurant table fading to warm red"></div>

  <section class="menu-card breakfast">
    <h3 class="section-title" style="margin-top:0">Acai Bowl</h3>
    <p class="dish-desc" style="color:var(--red)">Choice of:</p>
    <ul class="acai-list">
      <li><span class="num">1</span><span><b>Zesty Detox</b> – Acai puree, frozen raspberries, banana, apple juice with garnish on top</span></li>
      <li><span class="num">2</span><span><b>Antioxidant</b> – Acai puree, frozen berries, avocado, coconut water with garnish on top</span></li>
      <li><span class="num">3</span><span><b>Tropical Feel</b> – Acai puree, frozen mango, coconut water with garnish on top</span></li>
      <li><span class="num">4</span><span><b>Coconut Kiss</b> – Acai puree, coconut, banana, coconut water with garnish on top</span></li>
    </ul>
    <div class="dish"><p class="dish-name">Eggs Benedict</p><p class="dish-desc">Poached eggs, English muffin, sautéed baby spinach served with hollandaise</p></div>
    <div class="dish"><p class="dish-name">Avocado Smash – V GF</p><p class="dish-desc">Feta, spinach &amp; avocado served on the sourdough</p></div>
    <div class="dish">
      <p class="dish-name">Add On's</p>
      <div class="price-row"><span class="label">Spinach</span><span class="leader"></span><span class="price">$5.00</span></div>
      <div class="price-row"><span class="label">Mushroom</span><span class="leader"></span><span class="price">$5.00</span></div>
      <div class="price-row"><span class="label">Egg</span><span class="leader"></span><span class="price">$5.00</span></div>
      <div class="price-row"><span class="label">Cheese</span><span class="leader"></span><span class="price">$5.00</span></div>
      <div class="price-row"><span class="label">Avocado</span><span class="leader"></span><span class="price">$5.00</span></div>
      <div class="price-row"><span class="label">Bacon</span><span class="leader"></span><span class="price">$5.00</span></div>
      <div class="price-row"><span class="label">Smoked salmon</span><span class="leader"></span><span class="price">$5.00</span></div>
    </div>
    <div class="dish"><p class="dish-name">Bruschetta</p><p class="dish-desc">Toast served with a mix of tangy tomatoes, basil, red onion and garlic with feta cheese and balsamic Italian dressing as garnish.</p></div>
    <div class="dish"><p class="dish-name">7-Seed Breakfast</p><p class="dish-desc">Deliciously toasted seven-seed low gluten bread topped with pesto sauce, served with ham, scrambled egg, leaf salad, sundried &amp; cherry tomatoes and feta cheese</p></div>
    <h3 class="section-title">Main</h3>
    <div class="dish" style="margin-top:2px"><p class="dish-name">Salmon Skin On</p><p class="dish-desc">Salmon fillet on the skin, grilled – THE WAY YOU LIKE IT. Served with choice of garden salad – steamed vegetables – rice. ADD Sauce – hollandaise, lemon butter</p></div>
    <div class="dish"><p class="dish-name">Steak of the Day</p><p class="dish-desc">Steak of the day cooked (rare, medium or well done). Served with TWO choices: chips – garden salad – steamed vegetables. ADD Sauce – Pepper, Mushroom OR Garlic</p></div>
  </section>

  <div class="photo fries" role="img" aria-label="Photo of club sandwich with golden fries"></div>

  <section class="menu-card lunch">
    <h3 class="section-title" style="margin-top:0">Salad</h3>
    <div class="dish" style="margin-top:2px"><p class="dish-name">Asian Chicken Fusion Salad</p><p class="dish-desc">Grilled chicken served with a medley of fresh salad greens, sesame nut crumb and a light sweet chilli, sesame and soy dressing</p></div>
    <div class="dish"><p class="dish-name">Caesar Salad</p><p class="dish-desc">Baby Cos lettuce, crispy bacon, garlic croutons, flaked parmesan cheese, boiled egg in Caesar dressing</p>
      <div class="price-row"><span class="label">Add chicken</span><span class="leader"></span><span class="price">$4.00</span></div>
      <div class="price-row"><span class="label">Smoked salmon</span><span class="leader"></span><span class="price">$5.00</span></div>
    </div>
    <div class="dish"><p class="dish-name">House Salad</p><p class="dish-desc">Crispy lettuce mix, tomato, cucumber, spinach, red onion, Kalamata olives and feta cheese with house dressing</p>
      <div class="price-row"><span class="label">Add chicken</span><span class="leader"></span><span class="price">$4.00</span></div>
      <div class="price-row"><span class="label">Smoked salmon</span><span class="leader"></span><span class="price">$5.00</span></div>
    </div>
    <h3 class="section-title">Pasta</h3>
    <div class="dish" style="margin-top:2px"><p class="dish-name">Fettuccine Carbonara</p><p class="dish-desc">Fettuccine with pan seared sliced ham, bacon, shallots and onion in a creamy garlic sauce</p></div>
    <div class="dish"><p class="dish-name">Fettuccine Matriciana – V</p><p class="dish-desc">Sun dried tomatoes, capsicum, zucchini, mushroom, onion and garlic in a Napoli sauce</p></div>
    <div class="dish"><p class="dish-name">Spaghetti Bolognese</p><p class="dish-desc">Spaghetti cooked al dente, pan tossed with a traditional Italian meat sauce</p></div>
    <h3 class="section-title">Breakfast</h3>
    <div class="dish" style="margin-top:2px"><p class="dish-name">Big Veranda Breakfast</p><p class="dish-desc">Sourdough OR Turkish served with eggs, bacon, chipolatas, hash brown, spinach, tomato &amp; mushroom</p></div>
  </section>

  <div class="brand small"><span class="name">Veranda</span><span class="sub">RESTAURANT</span></div>

  <div class="photo salad" role="img" aria-label="Photo of a fresh green salad bowl with grated carrot"></div>
  <div class="photo steak" role="img" aria-label="Photo of glazed meat with broccoli and parmesan crisp"></div>

  <svg class="rings" width="1140" height="880" viewBox="0 0 1140 880" aria-hidden="true">
    <circle cx="792" cy="380" r="154" fill="none" stroke="#1d1d1d" stroke-width="2"/>
    <circle cx="792" cy="380" r="134" fill="#111"/>
    <circle cx="610" cy="667" r="106" fill="none" stroke="#1d1d1d" stroke-width="2"/>
    <circle cx="490" cy="775" r="96" fill="none" stroke="#1d1d1d" stroke-width="2"/>
    <circle cx="140" cy="790" r="112" fill="none" stroke="#1d1d1d" stroke-width="2"/>
  </svg>

  <div class="brand cover"><span class="name">Veranda</span><span class="sub">RESTAURANT</span></div>
  <div class="headline"><span class="light">A RELAXED</span><span class="bold">BISTRO</span></div>
  <div class="web">www.verandabistro.com</div>

  <div class="contact">
    <h2>CONTACT US</h2>
    <div class="contact-row">
      <svg viewBox="0 0 24 24"><path fill="#e3262f" d="M6.6 10.8a15 15 0 0 0 6.6 6.6l2.2-2.2c.3-.3.7-.4 1-.2 1.1.4 2.3.6 3.6.6.6 0 1 .4 1 1V20c0 .6-.4 1-1 1A17 17 0 0 1 3 4c0-.6.4-1 1-1h3.5c.6 0 1 .4 1 1 0 1.3.2 2.5.6 3.6.1.3 0 .7-.2 1z"/></svg>
      <span>07 5550 0182</span></div>
    <div class="contact-row">
      <svg viewBox="0 0 24 24"><rect x="2" y="5" width="20" height="14" rx="2" fill="#e3262f"/><path d="M3 6l9 7 9-7" fill="none" stroke="#111" stroke-width="1.8"/></svg>
      <span>hello@verandabistro.com</span></div>
    <div class="contact-row">
      <svg viewBox="0 0 24 24"><path fill="#e3262f" d="M12 2a7 7 0 0 0-7 7c0 5 7 13 7 13s7-8 7-13a7 7 0 0 0-7-7zm0 9.5A2.5 2.5 0 1 1 12 6.5a2.5 2.5 0 0 1 0 5z"/></svg>
      <span>Corner of Elm<br>&amp; Harbour Road<br>Westvale</span></div>
    <div class="contact-row">
      <svg viewBox="0 0 24 24"><circle cx="12" cy="12" r="9" fill="none" stroke="#e3262f" stroke-width="2"/><path d="M3 12h18M12 3c3 3 3 15 0 18M12 3c-3 3-3 15 0 18" fill="none" stroke="#e3262f" stroke-width="1.6"/></svg>
      <span>www.verandabistro.com</span></div>
  </div>

  <div class="hero-dish" role="img" aria-label="Photo of loaded nachos with guacamole, sour cream, salsa and coriander on a white plate"></div>

  <div class="fold" style="left:380px"></div>
  <div class="fold" style="left:760px"></div>
</div>
</body>
</html>
```